2-Sided Flyer for Printing - Quarvelent

We are looking for the most attractive and best quality flyer to serve as a handout to distribute as a printed document in fairs and conventions. We want one A4 sheet using two sides to display what is Quarvelent in an attractive and simple way.
• What is Quarvelent, what we do and benefits
o Type of challenges we solve
o Benefit for the companies
o Benefit for the solvers (engineers)
• How does it work
• Sample challenges
• Show our Community (skills, solvers pictures, etc)
The flyer should be developed according to our corporate colours (see landing page and logo)
The material we are uploading is the following:
• Power point with the introduction to Quarvelent
• Sample non professional flyers
• In addition you can use any material available through our web: www.quarvelent-example.com (landing page, blog, clients pages, ranking, etc.)

Target Market(s)

industrial companies and engineers

Industry/Entity Type

Engineering

Requirements
Must have
• A single flyer to be used for companies (clients) and engineers (solvers)
• overall flyer creative design
• clear and clean messages
• contain what is Quarvelent, how it works, community and sample challenges
• social networks info
• corporate pallet
Nice to have
• attractive funnel design to show how to move from a challenge to unique solutions
• attractive way to show the crowd using real solvers pictures
• Not all the background should be coloured (combination of white and corporate colours)
Should not have
• Copy and paste of the provided information and pictures
• High density content
• We do not like the design of the file "Brochure OK final.pdf" and we are looking for a 2-sided flyer

```html
<!DOCTYPE html>
<html lang="en">
<head>
<meta charset="utf-8">
<title>Quarvelent – Sample Challenges</title>
<link href="https://fonts.googleapis.com/css2?family=Montserrat:wght@600&family=Roboto+Condensed:wght@400&family=Work+Sans:wght@400;500&family=Roboto:wght@500&display=swap" rel="stylesheet">
<style>
  :root{
    --page-bg:#e9e7ec;
    --paper:#ffffff;
    --ink:#333333;
    --blue:#29a8e0;
    --orange:#f15a24;
    --teal:#2bb596;
    --btn-one:#3b5998;
    --btn-two:#0a74b2;
    --btn-three:#dd4b39;
    --btn-four:#23a9e1;
    --white:#ffffff;
  }
  *{box-sizing:border-box;margin:0;padding:0}
  html,body{width:1040px;height:1200px;overflow:hidden;background:var(--page-bg)}
  .flyer{
    position:absolute;left:68px;top:15px;
    width:837px;height:1083px;
    background:var(--paper);
    transform:scale(1.08);transform-origin:top left;
    font-family:"Work Sans",sans-serif;
  }
  .header{position:absolute;left:0;top:0;width:837px;height:116px}
  .brand{position:absolute;left:37px;top:58px;display:flex;align-items:center;gap:7px}
  .brand-dot{width:12px;height:12px;border-radius:50%;background:var(--blue)}
  .brand-name{font-family:"Work Sans",sans-serif;font-weight:400;font-size:17px;color:var(--ink);letter-spacing:.5px}
  .page-title{position:absolute;left:0;width:775px;text-align:center;top:64px;
    font-family:"Montserrat",sans-serif;font-weight:600;font-size:20px;letter-spacing:-.3px;color:#3a3a3a}
  .site-url{position:absolute;right:41px;top:68px;font-size:14.5px;letter-spacing:.8px;color:#222}

  .challenge{position:absolute;left:0;width:837px;height:258px;display:flex}
  .challenge.one{top:116px}
  .challenge.two{top:412px}
  .challenge.three{top:708px}
  .panel{width:413px;height:100%;padding:28px 30px 0 37px;color:var(--white)}
  .panel.blue{background:var(--blue)}
  .panel.orange{background:var(--orange);width:423px;padding-left:32px}
  .panel.teal{background:var(--teal)}
  .panel h2{font-family:"Roboto Condensed",sans-serif;font-weight:400;font-size:18px;line-height:23px;text-transform:uppercase;margin-bottom:11px}
  .panel p{font-size:12.6px;line-height:20.6px;letter-spacing:.6px;font-weight:400}
  .panel p + p{margin-top:18px}
  .photo{flex:1;height:100%}
  .photo.bottles{background:linear-gradient(160deg,#e4e8ee 0%,#b9c2cc 45%,#3c4a8e 75%,#d8dde4 100%)}
  .photo.foundry{background:radial-gradient(ellipse at 45% 35%,#ffb13b 0%,#e2521d 22%,#6a5a55 50%,#3b3b3d 100%)}
  .photo.tubes{background:linear-gradient(170deg,#9aa0a6 0%,#c9ccce 40%,#7d8287 75%,#5d6166 100%)}

  .sign-in{position:absolute;left:28px;top:1018px;display:flex;gap:11px}
  .sign-btn{width:187px;height:37px;display:flex;align-items:center;color:var(--white);
    font-family:"Roboto",sans-serif;font-weight:500;font-size:12.5px}
  .sign-btn .mark{width:34px;height:100%;display:flex;align-items:center;justify-content:center;border-right:1px solid rgba(0,0,0,.15)}
  .sign-btn .mark span{width:14px;height:14px;background:rgba(255,255,255,.9)}
  .sign-btn .label{padding-left:9px;white-space:nowrap}
  .sign-btn.one{background:var(--btn-one)}
  .sign-btn.two{background:var(--btn-two)}
  .sign-btn.three{background:var(--btn-three)}
  .sign-btn.four{background:var(--btn-four);font-size:11.5px;letter-spacing:-.2px}
</style>
</head>
<body>
<div class="flyer">
  <header class="header">
    <div class="brand"><span class="brand-dot"></span><span class="brand-name">Quarvelent</span></div>
    <h1 class="page-title">SAMPLE CHALLENGES</h1>
    <div class="site-url">www.quarvelent-example.com</div>
  </header>

  <section class="challenge one">
    <div class="panel blue">
      <h2>Eco friendly packaging design<br>challenge (8K in prizes)</h2>
      <p>The packaging of bottled water is usually made of a film of plastic material. The pack contains 6 bottles of water of 1.5 liters each. This plastic material is a shrink-wrap film, which is thermo-retracted with heat. The objective of this challenge is to replace the use of plastic materials in their products.</p>
    </div>
    <div class="photo bottles" role="img" aria-label="Close-up photo of plastic water bottles with blue caps"></div>
  </section>

  <section class="challenge two">
    <div class="photo foundry" role="img" aria-label="Photo of molten steel being poured from a ladle in a steel plant"></div>
    <div class="panel orange">
      <h2>Automatic alignment system<br>project (10 K € in prizes)</h2>
      <p>This is the process our client follows to produce steel tubes or beams: a spoon is placed over a filling sprue, acting as an elevated funnel in which the steel is poured down to fill up the ingot molds. This process is intuitively performed by the crane operator.</p>
    </div>
  </section>

  <section class="challenge three">
    <div class="panel teal">
      <h2>The productivity project for<br>tubes packing (8-12K € in prizes)</h2>
      <p>The manufacturing process of steel tubes requires the involvement of too many workers.</p>
      <p>In fact, at the end of the manufacturing line, tubes accumulate before they are taken to the storage location for the finished product. The batches arrive discontinually and the tubes intertwine with each other.</p>
    </div>
    <div class="photo tubes" role="img" aria-label="Photo of bundled steel tubes stacked in a warehouse"></div>
  </section>

  <nav class="sign-in">
    <div class="sign-btn one"><div class="mark"><span></span></div><div class="label">Log in with Circlespace</div></div>
    <div class="sign-btn two"><div class="mark"><span></span></div><div class="label">Sign in with Linkwork</div></div>
    <div class="sign-btn three"><div class="mark"><span></span></div><div class="label">Sign in with Searchly</div></div>
    <div class="sign-btn four">
      <div class="mark">
        <svg width="20" height="16" viewBox="0 0 20 16" aria-hidden="true"><rect x="1" y="1" width="18" height="14" rx="1.5" fill="none" stroke="#fff" stroke-width="1.8"/><path d="M1.5 2 L10 9 L18.5 2" fill="none" stroke="#fff" stroke-width="1.8"/></svg>
      </div>
      <div class="label">Register using your email</div>
    </div>
  </nav>
</div>
</body>
</html>
```